Start a weight loss Clinic

build a landing page website using the content from this websites. we want to copy all the content from slimpathcoaching.net but make page look more professional. we dont have a logo yet but url is www.brightvitalitycentre.com
https://clinicwellnessalliancegroup.net/home-page
https://www.slimpathcoaching.net/

Target Market(s)

people looking to open a weightloss clinic or a franchise opportunity

Coding

Number of Pages Required

3 page

Requirements
Must have
• copy all content from other site https://www.slimpathcoaching.net/

```html
<!DOCTYPE html>
<html lang="en">
<head>
<meta charset="utf-8">
<title>Bright Vitality Centre – Start Your Own Weight Loss Clinic</title>
<link href="https://fonts.googleapis.com/css2?family=Poppins:wght@400;500;600;700&display=swap" rel="stylesheet">
<style>
:root{
  --navy:#0f3a84;
  --navy-dark:#0b2f6e;
  --red:#c7161e;
  --ink:#1d2b4f;
  --muted:#51607e;
  --white:#ffffff;
  --line:#d9dee8;
  --badge:#e4e7ee;
}
*{margin:0;padding:0;box-sizing:border-box}
html,body{width:1200px;height:4237px;overflow:hidden}
body{font-family:'Poppins',sans-serif;color:var(--ink);background:var(--white);position:relative}
svg{display:block}
.abs{position:absolute}
.btn{position:absolute;display:flex;align-items:center;justify-content:center;border-radius:30px;font-weight:600;font-size:13px;color:var(--white);background:var(--red);text-decoration:none}
.btn--white{background:var(--white);color:var(--navy)}
.round-icon{display:grid;place-items:center;border-radius:50%;flex:none}

/* hero */
.hero{position:absolute;left:0;top:0;width:1200px;height:638px;background:linear-gradient(90deg,#f4f4f6 0%,#f7f3f4 45%,#e8e4e4 100%);border-top:4px solid var(--red);overflow:hidden}
.hero__photo{position:absolute;left:520px;top:0;width:680px;height:638px;background:linear-gradient(100deg,rgba(244,244,246,0) 0%,#d9dde3 25%,#c9cfd8 60%,#e9e6e6 100%)}
.brand{position:absolute;display:flex;align-items:center;gap:8px;font-weight:600;color:var(--navy);white-space:nowrap}
.brand__dot{border-radius:50%;border:2px solid var(--navy);flex:none}
.hero .brand{left:168px;top:30px;font-size:18px}
.hero .brand__dot{width:30px;height:30px}
.appt{position:absolute;left:815px;top:25px;width:214px;height:46px;border-radius:24px;background:var(--red);color:var(--white);display:flex;align-items:center;padding-left:12px;gap:12px}
.appt__icon{width:32px;height:32px;background:var(--white)}
.appt small{display:block;font-size:9px;font-weight:600;letter-spacing:.5px;line-height:1.1}
.appt strong{display:block;font-size:16px;font-weight:600;line-height:1.2}
.hero__kicker{left:168px;top:203px;font-size:12px;font-weight:600;letter-spacing:1.5px;color:var(--red)}
.hero__title{left:166px;top:216px;font-size:56px;font-weight:700;line-height:66px;color:var(--navy)}
.hero__title .red{color:var(--red)}

/* partners */
.partner{position:absolute;top:720px;width:242px;height:130px;border:1px solid var(--line);background:var(--white);display:flex;align-items:center;justify-content:center}
.partner--active{border:2px solid var(--red);box-shadow:0 4px 12px rgba(0,0,0,.15)}
.partner__badge{width:150px;height:70px;border-radius:8px;background:var(--badge)}

/* offer */
.offer{position:absolute;left:0;top:932px;width:1200px;height:503px;background:linear-gradient(135deg,var(--navy) 0%,#123f8c 60%,var(--navy-dark) 100%)}
.section-title{position:absolute;width:100%;text-align:center;font-weight:600}
.offer .section-title{top:74px;font-size:38px;color:var(--white)}
.card{position:absolute;top:155px;width:225px;height:266px;background:var(--white);text-align:center}
.card--active{background:var(--red)}
.card__icon{position:absolute;left:62px;top:30px;width:100px;height:100px;background:var(--navy);border:4px solid var(--red)}
.card--active .card__icon{background:var(--red);border-color:var(--white)}
.card__label{position:absolute;left:10px;right:10px;top:147px;font-size:16px;line-height:20px;color:var(--navy)}
.card--active .card__label{color:var(--white)}
.card .btn{left:55px;top:205px;width:115px;height:31px;font-size:12px}

/* welcome */
.welcome__photo{left:169px;top:1517px;width:471px;height:489px;background:linear-gradient(160deg,#cfd6df 0%,#b8c2cd 40%,#e8ebe6 70%,#a9c08d 100%)}
.welcome__inset{left:276px;top:1785px;width:256px;height:240px;background:linear-gradient(180deg,#f1ebe8,#d9d3d2);border:4px solid var(--white)}
.watch{left:502px;top:1517px;width:138px;height:100px;background:var(--white);text-align:center;font-size:16px;line-height:18px;color:var(--navy);padding-top:24px}
.watch__play{display:block;margin:10px auto 0;width:32px;height:32px;border-radius:50%;background:var(--red)}
.welcome__kicker{left:681px;top:1556px;font-size:11px;font-weight:600;letter-spacing:1.5px;color:var(--navy)}
.welcome__title{left:680px;top:1570px;font-size:31px;font-weight:600;color:var(--navy)}
.welcome__sub{left:681px;top:1613px;font-size:19px;color:var(--red)}
.welcome__text{left:681px;width:370px;font-size:12.5px;line-height:20px;color:var(--muted)}
.welcome__text b{color:var(--navy);font-weight:600}
.welcome__happy{left:681px;top:1914px;font-size:15px;color:var(--red)}
.link-ask{left:681px;top:1968px;font-size:12px;font-weight:600;color:var(--red);text-decoration:underline}

/* compare */
.compare{position:absolute;left:0;top:2106px;width:554px;height:526px;background:var(--navy)}
.compare__photo{left:554px;top:2106px;width:646px;height:526px;background:linear-gradient(90deg,#e9d7c8 0%,#d8bba4 45%,#cfb099 70%,#e4d7cc 100%)}
.compare__title{left:168px;top:74px;font-size:38px;font-weight:600;color:var(--white)}
.compare__list{position:absolute;left:168px;top:126px;list-style:none}
.compare__list li{display:flex;align-items:center;gap:6px;height:33px;font-size:19px;color:var(--white)}
.compare .btn{left:168px;top:411px;width:148px;height:32px;font-size:12px}

/* get started */
.kicker-red{width:100%;text-align:center;top:2711px;font-size:12px;font-weight:600;letter-spacing:1.5px;color:var(--red)}
.start-title{top:2724px;font-size:38px;color:var(--navy)}
.step__photo{position:absolute;top:2806px;width:274px;height:274px;border-radius:50%}
.step__bar{position:absolute;top:3004px;width:278px;height:51px;display:flex;align-items:center;justify-content:center;font-size:20px;font-weight:600;color:var(--white);background:var(--navy)}
.step__bar--red{background:var(--red)}

/* contact */
.touch-title{top:3150px;font-size:38px;color:var(--navy)}
.info__title{left:168px;top:3272px;font-size:32px;font-weight:600;color:var(--navy)}
.info__item{position:absolute;left:168px;display:flex;gap:14px}
.info__icon{width:42px;height:42px;background:var(--red)}
.info__item strong{display:block;font-size:13px;font-weight:600;color:var(--red);line-height:18px}
.info__item span{display:block;font-size:14px;color:var(--navy);line-height:18px}

.footer{position:absolute;left:0;top:3676px;width:1200px;height:561px;background:var(--navy)}
.form{position:absolute;left:625px;top:3232px;width:486px;height:587px;background:var(--white);box-shadow:0 4px 20px rgba(0,0,0,.12);border:1px solid #e3e6ec}
.form__title{position:absolute;width:100%;top:36px;text-align:center;font-size:31px;font-weight:600;color:var(--navy)}
.field{position:absolute;left:31px;width:419px;height:53px;border:1px solid var(--line);font-size:12px;color:var(--muted);padding:16px 20px}
.form .btn{left:149px;top:482px;width:184px;height:56px;font-size:13px}

.social{position:absolute;top:52px;width:49px;height:49px;border-radius:50%;background:rgba(255,255,255,.12);border:1px solid rgba(255,255,255,.25)}
.footer .brand{left:0;width:100%;justify-content:center;top:216px;font-size:30px;color:var(--white)}
.footer .brand__dot{width:50px;height:50px;border-color:var(--white)}
.nav{position:absolute;top:312px;left:0;width:100%;display:flex;justify-content:center;list-style:none}
.nav li{font-size:12px;color:var(--white);padding:0 30px}
.rule{position:absolute;left:60px;width:1080px;height:1px;background:rgba(255,255,255,.25)}
.fcontact{position:absolute;top:390px;display:flex;align-items:center;gap:26px;color:var(--white)}
.fcontact__icon{width:77px;height:77px;background:rgba(255,255,255,.15)}
.fcontact strong{display:block;font-size:13px;font-weight:500;line-height:20px}
.fcontact span{display:block;font-size:14px;line-height:18px}
.copyright{position:absolute;top:524px;width:100%;text-align:center;font-size:11px;color:var(--white)}
</style>
</head>
<body>

<header class="hero">
  <div class="hero__photo" role="img" aria-label="Photo of a smiling doctor weighing a young woman on a clinic scale"></div>
  <div class="brand"><span class="brand__dot"></span>Bright Vitality Centre</div>
  <div class="appt">
    <span class="round-icon appt__icon"><svg width="16" height="16" viewBox="0 0 24 24"><path fill="#c7161e" d="M6.6 10.8a15 15 0 0 0 6.6 6.6l2.2-2.2c.3-.3.7-.4 1-.2 1.1.4 2.3.6 3.6.6.6 0 1 .4 1 1V20c0 .6-.4 1-1 1A17 17 0 0 1 3 4c0-.6.4-1 1-1h3.5c.6 0 1 .4 1 1 0 1.3.2 2.5.6 3.6.1.3 0 .7-.2 1z"/></svg></span>
    <span><small>MAKE AN APPOINTMENT</small><strong>(555) 014-2236</strong></span>
  </div>
  <p class="abs hero__kicker">START YOUR OWN</p>
  <h1 class="abs hero__title">PROFITABLE<br><span class="red">WEIGHT LOSS</span><br>CLINIC!</h1>
  <a class="btn" style="left:169px;top:432px;width:135px;height:31px">Contact Us</a>
</header>

<section>
  <div class="partner" style="left:192px"><div class="partner__badge" role="img" aria-label="Accreditation badge"></div></div>
  <div class="partner partner--active" style="left:478px"><div class="partner__badge" role="img" aria-label="Professional membership badge"></div></div>
  <div class="partner" style="left:765px"><div class="partner__badge" role="img" aria-label="Medical society membership badge"></div></div>
</section>

<section class="offer">
  <h2 class="section-title">What We Offer</h2>
  <div class="card card--active" style="left:133px">
    <div class="round-icon card__icon"><svg width="44" height="44" viewBox="0 0 44 44" fill="none" stroke="#fff" stroke-width="2"><rect x="6" y="4" width="32" height="20"/><circle cx="14" cy="30" r="4"/><circle cx="30" cy="30" r="4"/><path d="M6 42c0-5 4-8 8-8s8 3 8 8M22 42c0-5 4-8 8-8s8 3 8 8"/></svg></div>
    <p class="card__label">One-on-one business &amp; medical training</p>
    <a class="btn btn--white">Read More</a>
  </div>
  <div class="card" style="left:370px">
    <div class="round-icon card__icon"><svg width="44" height="44" viewBox="0 0 44 44" fill="none" stroke="#fff" stroke-width="2"><rect x="4" y="6" width="14" height="10"/><rect x="26" y="6" width="14" height="10"/><rect x="4" y="28" width="14" height="10"/><rect x="26" y="28" width="14" height="10"/><path d="M18 11h8M11 16v12M33 16v12"/></svg></div>
    <p class="card__label">Marketing &amp; Advertising Training</p>
    <a class="btn">Read More</a>
  </div>
  <div class="card" style="left:605px">
    <div class="round-icon card__icon"><svg width="44" height="44" viewBox="0 0 44 44" fill="none" stroke="#fff" stroke-width="2"><rect x="8" y="4" width="28" height="36"/><path d="M22 14v14M15 21h14"/></svg></div>
    <p class="card__label">Diets, Patient Protocols &amp; Programs</p>
    <a class="btn">Read More</a>
  </div>
  <div class="card" style="left:842px">
    <div class="round-icon card__icon"><svg width="44" height="44" viewBox="0 0 44 44" fill="none" stroke="#fff" stroke-width="2"><rect x="8" y="4" width="24" height="34"/><path d="M13 12h14M13 18h14M13 24h10"/></svg></div>
    <p class="card__label">Office &amp; Operations Manuals</p>
    <a class="btn">Read More</a>
  </div>
</section>

<section>
  <div class="abs welcome__photo" role="img" aria-label="Photo of a laptop with a diet chart, a clipboard and a plant"></div>
  <div class="abs welcome__inset" role="img" aria-label="Photo of a nurse measuring a patient's waist with a tape"></div>
  <div class="abs watch">Watch<br>Video<span class="watch__play"><svg width="32" height="32"><path d="M13 10l9 6-9 6z" fill="#fff"/></svg></span></div>
  <p class="abs welcome__kicker">WELCOME THERE!</p>
  <h2 class="abs welcome__title">Start Your Own</h2>
  <p class="abs welcome__sub">Weight Loss &amp; Wellness Center</p>
  <p class="abs welcome__text" style="top:1654px">Bright Vitality Centre now offers our model to you so you can add <b>weight loss and wellness programs</b> to your existing medical practice or open a stand alone weight loss and wellness center.</p>
  <p class="abs welcome__text" style="top:1754px">We are not a <b>weight loss franchise – you are simply buying our business model,</b> training and support for one low fee. Please read about us, look at what we offer and compare us to <b>weight loss franchises</b> in the marketplace.</p>
  <p class="abs welcome__text" style="top:1854px">We now offer you a free market analysis and sample break even analysis for your area. <b>Please see our contact page.</b></p>
  <p class="abs welcome__happy">We think you will be happy you found us!</p>
  <a class="abs link-ask">Ask An Expert</a>
  <a class="btn" style="left:778px;top:1960px;width:111px;height:34px;font-size:11px">More Info</a>
</section>

<section class="compare">
  <h2 class="abs compare__title">Our COMPARE</h2>
  <ul class="compare__list">
    <li><svg width="14" height="14" viewBox="0 0 14 14" fill="none" stroke="#fff" stroke-width="1.3"><circle cx="7" cy="7" r="6"/><path d="M4 7l2 2 4-4"/></svg>No franchise fees</li>
    <li><svg width="14" height="14" viewBox="0 0 14 14" fill="none" stroke="#fff" stroke-width="1.3"><circle cx="7" cy="7" r="6"/><path d="M4 7l2 2 4-4"/></svg>No Territory fees</li>
    <li><svg width="14" height="14" viewBox="0 0 14 14" fill="none" stroke="#fff" stroke-width="1.3"><circle cx="7" cy="7" r="6"/><path d="M4 7l2 2 4-4"/></svg>No monthly licensing fees</li>
    <li><svg width="14" height="14" viewBox="0 0 14 14" fill="none" stroke="#fff" stroke-width="1.3"><circle cx="7" cy="7" r="6"/><path d="M4 7l2 2 4-4"/></svg>No % advertising fees</li>
    <li><svg width="14" height="14" viewBox="0 0 14 14" fill="none" stroke="#fff" stroke-width="1.3"><circle cx="7" cy="7" r="6"/><path d="M4 7l2 2 4-4"/></svg>No scope of practice limits</li>
    <li><svg width="14" height="14" viewBox="0 0 14 14" fill="none" stroke="#fff" stroke-width="1.3"><circle cx="7" cy="7" r="6"/><path d="M4 7l2 2 4-4"/></svg>No convention fees</li>
    <li><svg width="14" height="14" viewBox="0 0 14 14" fill="none" stroke="#fff" stroke-width="1.3"><circle cx="7" cy="7" r="6"/><path d="M4 7l2 2 4-4"/></svg>No % royalties</li>
    <li><svg width="14" height="14" viewBox="0 0 14 14" fill="none" stroke="#fff" stroke-width="1.3"><circle cx="7" cy="7" r="6"/><path d="M4 7l2 2 4-4"/></svg>No mandatory vendors</li>
  </ul>
  <a class="btn">Compare Now!</a>
</section>
<div class="abs compare__photo" role="img" aria-label="Photo of a slim waist wrapped in a yellow measuring tape"></div>

<section>
  <p class="abs kicker-red">IT'S EASY</p>
  <h2 class="section-title start-title">GET STARTED TODAY</h2>
  <div class="step__photo" style="left:145px;background:linear-gradient(160deg,#6f8f5a,#2f3b2c)" role="img" aria-label="Photo of hands holding a smartphone"></div>
  <div class="step__photo" style="left:463px;background:linear-gradient(180deg,#d9a14a,#8a4a34 60%,#b49d86)" role="img" aria-label="Photo of a visitor walking towards a brick building"></div>
  <div class="step__photo" style="left:781px;background:linear-gradient(160deg,#e9ecef,#aab4bf)" role="img" aria-label="Photo of a person joining a video webinar on a monitor"></div>
  <div class="step__bar" style="left:143px">Contact Us</div>
  <div class="step__bar step__bar--red" style="left:461px">Visit Us</div>
  <div class="step__bar" style="left:779px">Schedule A Webinar</div>
</section>

<section>
  <h2 class="section-title touch-title">Get In Touch</h2>
  <h3 class="abs info__title">CONTACT INFOMATION</h3>
  <div class="info__item" style="top:3334px">
    <span class="round-icon info__icon"><svg width="18" height="14" viewBox="0 0 18 14"><rect width="18" height="14" rx="2" fill="#fff"/><path d="M1 2l8 6 8-6" fill="none" stroke="#c7161e" stroke-width="1.5"/></svg></span>
    <div><strong>EMAIL:</strong><span>info@slimpathcoaching.net</span></div>
  </div>
  <div class="info__item" style="top:3404px">
    <span class="round-icon info__icon"><svg width="16" height="20" viewBox="0 0 16 20"><path d="M8 0a8 8 0 0 1 8 8c0 6-8 12-8 12S0 14 0 8a8 8 0 0 1 8-8z" fill="#fff"/><circle cx="8" cy="8" r="3" fill="#c7161e"/></svg></span>
    <div><strong>ADDRESS:</strong><span>4410 Orchard Vale Road Suite 210,<br>Millbrook, GA 30999</span></div>
  </div>
  <div class="info__item" style="top:3476px">
    <span class="round-icon info__icon"><svg width="18" height="18" viewBox="0 0 24 24"><path fill="#fff" d="M6.6 10.8a15 15 0 0 0 6.6 6.6l2.2-2.2c.3-.3.7-.4 1-.2 1.1.4 2.3.6 3.6.6.6 0 1 .4 1 1V20c0 .6-.4 1-1 1A17 17 0 0 1 3 4c0-.6.4-1 1-1h3.5c.6 0 1 .4 1 1 0 1.3.2 2.5.6 3.6.1.3 0 .7-.2 1z"/></svg></span>
    <div><strong>CALL US:</strong><span>(555) 014-2236</span></div>
  </div>
</section>

<footer class="footer">
  <div class="social" style="left:170px"></div>
  <div class="social" style="left:228px"></div>
  <div class="social" style="left:287px"></div>
  <div class="social" style="left:351px"></div>
  <div class="brand"><span>Bright Vitality Centre</span><span class="brand__dot"></span></div>
  <ul class="nav"><li>HOME</li><li>ABOUT US</li><li>WHAT WE OFFER</li><li>COMPARE</li><li>FAQ</li><li>CONTACT</li></ul>
  <div class="rule" style="top:357px"></div>
  <div class="fcontact" style="left:85px">
    <span class="round-icon fcontact__icon"><svg width="22" height="28" viewBox="0 0 16 20"><path d="M8 0a8 8 0 0 1 8 8c0 6-8 12-8 12S0 14 0 8a8 8 0 0 1 8-8z" fill="#fff"/><circle cx="8" cy="8" r="3" fill="#0f3a84"/></svg></span>
    <div><strong>ADDRESS:</strong><span>4410 Orchard Vale Road Suite 210,<br>Millbrook, GA 30999</span></div>
  </div>
  <div class="fcontact" style="left:476px">
    <span class="round-icon fcontact__icon"><svg width="30" height="30" viewBox="0 0 24 24"><path fill="#fff" d="M6.6 10.8a15 15 0 0 0 6.6 6.6l2.2-2.2c.3-.3.7-.4 1-.2 1.1.4 2.3.6 3.6.6.6 0 1 .4 1 1V20c0 .6-.4 1-1 1A17 17 0 0 1 3 4c0-.6.4-1 1-1h3.5c.6 0 1 .4 1 1 0 1.3.2 2.5.6 3.6.1.3 0 .7-.2 1z"/></svg></span>
    <div><strong>CONTACT NO:</strong><span>(555) 014-2236</span></div>
  </div>
  <div class="fcontact" style="left:774px">
    <span class="round-icon fcontact__icon"><svg width="32" height="24" viewBox="0 0 18 14"><rect width="18" height="14" rx="2" fill="#fff"/><path d="M1 2l8 6 8-6" fill="none" stroke="#0f3a84" stroke-width="1.5"/></svg></span>
    <div><strong>EMAIL:</strong><span>info@slimpathcoaching.net</span></div>
  </div>
  <div class="rule" style="top:505px"></div>
  <p class="copyright">© 2023 Bright Vitality Centre, Inc. All rights reserved</p>
</footer>

<form class="form">
  <h3 class="form__title">CONTACT US</h3>
  <div class="field" style="top:96px">Name</div>
  <div class="field" style="top:159px">Email</div>
  <div class="field" style="top:221px">Phone</div>
  <div class="field" style="top:284px;height:153px">Messgae</div>
  <a class="btn">SUBMIT MESSAGE</a>
</form>

</body>
</html>
```